Redesign retirement planner website

Provide an original design for a website. The site should introduce the retirement planner, explain the basic offerings of his services, and invite the website visitor to enter their name, phone, and email. Please provide a ready-to-publish redesign that can actually be published via a Wordpress template or other major website builder like SquareSpace or Wix. Some introductory content is attached, but feel free to add additional sections/images/blocks/copywriting and rearrange/delete sections entirely to make your design original and compelling. Feel free to pull copywriting from here but again, do not use this original design, feel free to create an entirely NEW design and layout. lynx-mango-trel (dot) sitefolio (dot) com password: 1234 -- FINAL NOTE: Do not choose a stock photo of a man for the retirement planner. This website needs to work well with no photo of the retirement planner himself. Think of a non-face-focused design to win this competition.

Industry/Entity Type

Retirement planner personal website

Number of Pages Required

1 page

Font styles to use
Sans Serif
Decorative

Requirements
Must have
• Please provide a ready-to-publish redesign that can actually be published via a Wordpress template or other major website builder.

```html
<!DOCTYPE html>
<html lang="en">
<head>
<meta charset="utf-8">
<title>Darren Vollick — Counselor &amp; Retirement Specialist</title>
<link href="https://fonts.googleapis.com/css2?family=Abril+Fatface&family=Yeseva+One&family=Roboto:wght@300;400;500;700&display=swap" rel="stylesheet">
<style>
:root{
  --gold:#ffc400;
  --orange:#f28c1c;
  --orange-soft:#e89a3a;
  --cream:#fbdcb8;
  --card:#fdf0e2;
  --field:#fcdcb9;
  --ink:#2d2624;
  --grey:#6b6b6b;
  --footer:#3a2b28;
  --white:#ffffff;
}
*{box-sizing:border-box;margin:0;padding:0}
html,body{width:1200px;height:3796px;overflow:hidden}
body{font-family:"Roboto",sans-serif;color:var(--ink);background:var(--white);position:relative}
.abs{position:absolute}

/* nav */
.site-nav{position:absolute;top:0;left:0;width:1200px;height:68px;background:var(--white)}
.brand{left:52px;top:15px;display:flex;align-items:center;gap:10px;font-family:"Roboto",sans-serif;font-weight:700;font-size:18px;color:var(--ink)}
.brand-square{width:38px;height:38px;background:var(--ink);border-radius:4px}
.nav-link{top:22px;font-size:18px;color:#8a8a8a;display:flex;align-items:center;gap:8px}
.nav-link.active{color:var(--orange);font-weight:500}
.nav-btn{left:990px;top:13px;width:158px;height:40px;background:var(--gold);border-radius:8px;font-size:14px;font-weight:700;display:flex;align-items:center;justify-content:center;letter-spacing:.3px}

/* hero */
.hero{position:absolute;top:68px;left:0;width:1200px;height:712px;
  background:radial-gradient(ellipse at 62% 40%,#6a5a4c 0%,#3f3a30 35%,#1e2519 70%,#121810 100%)}
.hero-shade{position:absolute;inset:0;background:linear-gradient(90deg,rgba(0,0,0,.55),rgba(0,0,0,.15))}
.hero-kicker{left:103px;top:158px;color:var(--white);font-size:18px}
.hero-title{left:103px;top:185px;font-family:"Abril Fatface",serif;color:var(--gold);font-size:60px;line-height:50px;letter-spacing:1px}
.hero-rule{left:108px;top:301px;width:3px;height:188px;background:#8a7a5a}
.hero-sub{left:123px;top:301px;color:var(--gold);font-size:21px;font-weight:300}
.hero-copy{left:123px;top:376px;width:520px;color:var(--white);font-size:16px;line-height:22.5px}
.play-btn{left:1088px;top:623px;width:60px;height:61px;background:#000;display:flex;align-items:center;justify-content:center}

/* specialties */
.eyebrow{font-size:21px;color:var(--grey)}
.display{font-family:"Yeseva One",serif;color:var(--ink)}
.spec-item{width:380px}
.spec-title{display:flex;align-items:center;gap:26px;color:var(--orange);font-size:20px;margin-bottom:12px}
.spec-desc{font-size:14px;line-height:17.5px;color:var(--ink)}
.name-mark{font-family:"Yeseva One",serif;color:var(--orange-soft);font-size:64px}
.mark-shadow{height:8px;border-radius:50%;background:radial-gradient(ellipse,rgba(200,150,100,.45),rgba(200,150,100,0) 70%)}

/* offerings */
.offer-card{top:1812px;width:239px;height:241px;border:1.5px solid #f6c89a;border-radius:24px;background:var(--white);text-align:center}
.offer-card.active{background:var(--card)}
.offer-icon{margin-top:40px;height:56px}
.offer-name{margin-top:12px;color:var(--orange);font-size:29px;font-weight:500;line-height:36px}

/* faq */
.faq{position:absolute;top:2109px;left:0;width:1200px;height:780px;background:var(--cream)}
.faq-mark{left:540px;top:170px;font-family:"Yeseva One",serif;font-size:260px;color:rgba(232,150,60,.45)}
.faq-item{left:193px;width:814px;background:rgba(255,255,255,.75);border-radius:10px;display:flex;align-items:center;justify-content:space-between;padding:0 28px;font-size:19px;color:var(--ink)}
.faq-item.open{display:block;background:var(--white);padding:28px}
.faq-q{display:flex;justify-content:space-between;align-items:center;color:var(--orange);font-weight:500}
.faq-a{margin:36px 12px 0 32px;font-size:14px;line-height:17px;color:#555}

/* contact */
.field{height:56px;background:var(--field);border-radius:8px;box-shadow:0 3px 6px rgba(0,0,0,.12);font-size:14px;color:#e8923a;padding:0 28px;display:flex;align-items:center}
.check{left:109px;top:3387px;display:flex;align-items:center;gap:12px;font-size:14px}
.check-box{width:30px;height:30px;border:1.5px solid #999;border-radius:3px;background:var(--white)}
.send-btn{left:109px;top:3467px;width:348px;height:80px;background:var(--gold);border-radius:8px;box-shadow:0 5px 10px rgba(0,0,0,.18);display:flex;align-items:center;justify-content:center;gap:14px;font-size:21px;font-weight:700}

/* footer */
.site-footer{position:absolute;top:3670px;left:0;width:1200px;height:126px;background:var(--footer);color:var(--white)}
.footer-name{left:52px;top:14px;font-family:"Abril Fatface",serif;color:var(--gold);font-size:23px}
.footer-line{left:54px;display:flex;align-items:center;gap:12px;font-size:14px}
.social-dot{left:1094px;top:40px;width:54px;height:54px;border-radius:50%;background:var(--gold)}
</style>
</head>
<body>

<header class="site-nav">
  <div class="abs brand"><span class="brand-square"></span>Vollick</div>
  <div class="abs nav-link active" style="left:545px">Home</div>
  <div class="abs nav-link" style="left:626px">Specialties
    <svg width="18" height="12" viewBox="0 0 18 12"><path d="M2 2l7 7 7-7" fill="none" stroke="#8a8a8a" stroke-width="2"/></svg></div>
  <div class="abs nav-link" style="left:775px">Insurance Offers
    <svg width="18" height="12" viewBox="0 0 18 12"><path d="M2 2l7 7 7-7" fill="none" stroke="#8a8a8a" stroke-width="2"/></svg></div>
  <div class="abs nav-btn">CONTACT ME</div>
</header>

<section class="hero" role="img" aria-label="Photograph of an older couple sharing coffee at an outdoor table">
  <div class="hero-shade"></div>
  <div class="abs hero-kicker">I'm a</div>
  <h1 class="abs hero-title">Counselor &amp;<br>Retirement Specialist</h1>
  <div class="abs hero-rule"></div>
  <p class="abs hero-sub">with a unique approach to financial planning.</p>
  <p class="abs hero-copy">You have a lifetime of accomplishments. Learning about them is my extraordinary honor. When I meet clients to make a plan for their final years of work and savings, I understand my solemn privilege. Your capital is irreplaceable. My job is to maximize its benefit for your health, family, and legacy.</p>
  <div class="abs play-btn"><svg width="26" height="28" viewBox="0 0 26 28"><path d="M2 2l22 12-22 12z" fill="#fff"/></svg></div>
</section>

<section class="specialties">
  <div class="abs eyebrow" style="left:99px;top:837px">My specialties</div>
  <h2 class="abs display" style="left:99px;top:875px;font-size:64px">My specialties</h2>

  <div class="abs spec-item" style="left:125px;top:1020px">
    <div class="spec-title">Estate Planning <svg width="28" height="28" viewBox="0 0 28 28"><path d="M12 3H3v22h22v-9M16 3h9v9M25 3L13 15" fill="none" stroke="#f28c1c" stroke-width="2.4"/></svg></div>
    <p class="spec-desc">Ensure your legacy is protected with comprehensive estate planning. I will guide you through creating wills, trusts, and other essential documents to secure your assets for future generations, ensuring your wishes are honored.</p>
  </div>
  <div class="abs spec-item" style="left:562px;top:1020px">
    <div class="spec-title">Retirement Forecasting <svg width="28" height="28" viewBox="0 0 28 28"><path d="M12 3H3v22h22v-9M16 3h9v9M25 3L13 15" fill="none" stroke="#f28c1c" stroke-width="2.4"/></svg></div>
    <p class="spec-desc">Plan for a fulfilling retirement with our expert forecasting services. I will analyze your financial situation and future needs to develop a personalized strategy, helping you achieve your retirement goals with confidence.</p>
  </div>
  <div class="abs spec-item" style="left:125px;top:1194px">
    <div class="spec-title">Final Expense <svg width="28" height="28" viewBox="0 0 28 28"><path d="M12 3H3v22h22v-9M16 3h9v9M25 3L13 15" fill="none" stroke="#f28c1c" stroke-width="2.4"/></svg></div>
    <p class="spec-desc">Prepare for life's final expenses with peace of mind. My services help you plan for costs associated with end-of-life arrangements, alleviating financial stress for your loved ones during a difficult time.</p>
  </div>
  <div class="abs spec-item" style="left:562px;top:1194px">
    <div class="spec-title">Life Insurance <svg width="28" height="28" viewBox="0 0 28 28"><path d="M12 3H3v22h22v-9M16 3h9v9M25 3L13 15" fill="none" stroke="#f28c1c" stroke-width="2.4"/></svg></div>
    <p class="spec-desc">Safeguard your family's future with tailored life insurance solutions. I provide expert advice to help you choose the right coverage, ensuring financial security for your loved ones when they need it most.</p>
  </div>
  <div class="abs spec-item" style="left:125px;top:1368px">
    <div class="spec-title">Portfolio Evaluation <svg width="28" height="28" viewBox="0 0 28 28"><path d="M12 3H3v22h22v-9M16 3h9v9M25 3L13 15" fill="none" stroke="#f28c1c" stroke-width="2.4"/></svg></div>
    <p class="spec-desc">Maximize your investment potential with our thorough portfolio evaluation. I assess your current assets and provide strategic recommendations to enhance your financial growth and stability.</p>
  </div>

  <div class="abs name-mark" style="left:890px;top:1345px">Vollick</div>
  <div class="abs mark-shadow" style="left:915px;top:1512px;width:210px"></div>
</section>

<section class="offerings">
  <div class="abs eyebrow" style="left:0;width:1200px;text-align:center;top:1617px">Insurance</div>
  <h2 class="abs display" style="left:0;width:1200px;text-align:center;top:1655px;font-size:66px">Offerings</h2>

  <div class="abs offer-card active" style="left:152px">
    <svg class="offer-icon" width="50" height="56" viewBox="0 0 50 56"><circle cx="18" cy="14" r="11" fill="#f28c1c"/><path d="M2 54c0-16 7-24 16-24 6 0 10 2 13 6" fill="#f28c1c"/><circle cx="34" cy="40" r="13" fill="#f7a84a"/><path d="M34 27a13 13 0 0 1 0 26z" fill="#f28c1c"/></svg>
    <div class="offer-name">Whole and<br>Universal Life</div>
  </div>
  <div class="abs offer-card" style="left:480px">
    <svg class="offer-icon" width="60" height="56" viewBox="0 0 60 56"><rect x="24" y="12" width="30" height="6" rx="3" fill="#f7b36a"/><rect x="26" y="21" width="30" height="6" rx="3" fill="#f7b36a"/><rect x="24" y="30" width="30" height="6" rx="3" fill="#f7b36a"/><rect x="26" y="39" width="28" height="6" rx="3" fill="#f7b36a"/><circle cx="22" cy="28" r="16" fill="#f28c1c"/><circle cx="19" cy="28" r="11" fill="#f7b36a"/></svg>
    <div class="offer-name">Annuities</div>
  </div>
  <div class="abs offer-card" style="left:809px">
    <svg class="offer-icon" width="54" height="56" viewBox="0 0 54 56"><rect x="2" y="8" width="48" height="40" rx="4" fill="#f7b36a"/><rect x="2" y="8" width="48" height="12" rx="4" fill="#f28c1c"/><rect x="12" y="3" width="4" height="10" rx="2" fill="#f28c1c"/><rect x="36" y="3" width="4" height="10" rx="2" fill="#f28c1c"/><circle cx="40" cy="42" r="11" fill="#fdf0e2" stroke="#f28c1c" stroke-width="2"/><path d="M43 38h-5a2 2 0 0 0 0 4h4a2 2 0 0 1 0 4h-5M40 35v14" fill="none" stroke="#f28c1c" stroke-width="1.6"/></svg>
    <div class="offer-name">Term and<br>Final Expense</div>
  </div>
</section>

<section class="faq">
  <div class="abs faq-mark">V</div>
  <h2 class="abs display" style="left:0;width:1200px;text-align:center;top:50px;font-size:66px">FAQs</h2>
  <div class="abs faq-item" style="top:170px;height:93px">Why is portfolio evaluation important for retirement planning?
    <svg width="16" height="28" viewBox="0 0 16 28"><path d="M2 2l12 12L2 26" fill="none" stroke="#f28c1c" stroke-width="2.4"/></svg></div>
  <div class="abs faq-item" style="top:283px;height:93px">What are final expenses and why should I plan for them?
    <svg width="16" height="28" viewBox="0 0 16 28"><path d="M2 2l12 12L2 26" fill="none" stroke="#f28c1c" stroke-width="2.4"/></svg></div>
  <div class="abs faq-item open" style="top:397px;height:169px">
    <div class="faq-q">How does retirement forecasting help me plan for the future?
      <svg width="28" height="16" viewBox="0 0 28 16"><path d="M2 2l12 12L26 2" fill="none" stroke="#f28c1c" stroke-width="2.4"/></svg></div>
    <p class="faq-a">Retirement forecasting analyzes your current financial situation, expected income, and future needs to create a personalized strategy. This ensures you can meet your retirement goals with confidence and enjoy financial security throughout your retirement years.</p>
  </div>
  <div class="abs faq-item" style="top:588px;height:93px">What is the difference between Whole Life and Universal Life Insurance?
    <svg width="16" height="28" viewBox="0 0 16 28"><path d="M2 2l12 12L2 26" fill="none" stroke="#f28c1c" stroke-width="2.4"/></svg></div>
</section>

<section class="contact">
  <div class="abs eyebrow" style="left:109px;top:3007px;font-size:18px">Contact Me</div>
  <h2 class="abs display" style="left:109px;top:3036px;font-size:46px;font-weight:400;letter-spacing:1px">Allow me to introduce myself.</h2>
  <div class="abs field" style="left:109px;top:3141px;width:292px">First Name</div>
  <div class="abs field" style="left:425px;top:3141px;width:372px">Last Name</div>
  <div class="abs field" style="left:109px;top:3222px;width:688px">Email</div>
  <div class="abs field" style="left:109px;top:3303px;width:373px">Phone</div>
  <div class="abs check"><span class="check-box"></span>Sign up for news and updates</div>
  <div class="abs send-btn">SEND A MESSAGE
    <svg width="20" height="15" viewBox="0 0 20 15"><rect width="20" height="15" rx="1.5" fill="#2d2624"/><path d="M1 1l9 7 9-7" fill="none" stroke="#ffc400" stroke-width="1.6"/></svg></div>
  <div class="abs name-mark" style="left:855px;top:3390px">Vollick</div>
  <div class="abs mark-shadow" style="left:880px;top:3556px;width:200px"></div>
</section>

<footer class="site-footer">
  <div class="abs footer-name">Darren Vollick</div>
  <div class="abs footer-line" style="top:60px"><svg width="16" height="12" viewBox="0 0 16 12"><rect width="16" height="12" rx="1" fill="#fff"/><path d="M1 1l7 5 7-5" fill="none" stroke="#3a2b28" stroke-width="1.4"/></svg>dvollick@ashpointplan.com</div>
  <div class="abs footer-line" style="top:85px"><svg width="16" height="16" viewBox="0 0 16 16"><path d="M4 1l3 3-2 2c1 2 3 4 5 5l2-2 3 3-2 3C7 15 1 9 1 3z" fill="#fff"/></svg>(415) 555 - 0142</div>
  <div class="abs social-dot" aria-label="Professional profile link"></div>
</footer>

</body>
</html>
```